Corvane Project Services - Flyer

Project Breif:
I need a single page A4 Capability Statement, which will be used to market our services to prospective clients, both in print and via email PDF.
It needs to look professional and should incorporate the elements I have uploaded into files, these include:
Capability Statement Text
Corvane Services Company Logo
Additional Logo’s (Tools We Use)
Glimmer Bay Pics can be cut into the page
I have included examples of capability statements as a guide to what i am looking for.
Regards
Derek
Engineering Consulting

```html
<!DOCTYPE html>
<html lang="en">
<head>
<meta charset="utf-8">
<title>Corvane Project Services – Capability Statement</title>
<link href="https://fonts.googleapis.com/css2?family=Titillium+Web:wght@300;400;600&display=swap" rel="stylesheet">
<style>
  :root {
    --band: #86cbe9;
    --accent: #5ab8e0;
    --heading: #5d92cc;
    --tagline: #6c9fd6;
    --text: #858585;
    --text-strong: #4a4a4a;
    --navy: #1d2a4a;
    --page-line: #ececec;
  }
  * { box-sizing: border-box; margin: 0; padding: 0; }
  html, body {
    width: 1200px; height: 800px; overflow: hidden;
    background: #fff;
    font-family: "Titillium Web", sans-serif;
  }
  .flyer {
    position: absolute; left: 362px; top: 63px;
    width: 477px; height: 674px;
    background: #fff;
    border: 1px solid var(--page-line);
    overflow: hidden;
  }
  .tagline {
    position: absolute; left: 42px; top: 43px;
    font-size: 13.6px; line-height: 18.6px; font-weight: 300;
    color: var(--tagline);
  }
  .tagline strong { font-weight: 600; font-size: 15px; }
  .band { position: absolute; height: 6px; background: var(--band); }
  .band--top { left: 0; top: 106px; width: 252px; clip-path: polygon(0 0, 246px 0, 100% 100%, 0 100%); }
  .band--mid { right: 0; top: 241px; width: 178px; clip-path: polygon(0 0, 100% 0, 100% 100%, 6px 100%); }
  .band--bottom { left: 0; top: 549px; width: 252px; clip-path: polygon(0 0, 246px 0, 100% 100%, 0 100%); }

  .brand {
    position: absolute; left: 318px; top: 34px; width: 122px;
    text-align: center; color: var(--navy);
  }
  .brand__mark {
    width: 34px; height: 34px; border-radius: 50%;
    background: var(--heading); margin: 0 auto 6px;
  }
  .brand__name {
    font-size: 10.5px; font-weight: 600; letter-spacing: 0.6px; line-height: 11px;
    text-transform: uppercase;
  }
  .brand__sub { font-size: 7.5px; letter-spacing: 3.6px; }

  .hero {
    position: absolute; left: 0; top: 117px; width: 100%; height: 119px;
    background: linear-gradient(100deg, #e9eef3 0%, #c9d6e2 30%, #f3f5f8 55%, #b9c7d6 80%, #e7ecf2 100%);
  }

  .intro {
    position: absolute; top: 260px; width: 190px;
    font-size: 8px; line-height: 12px; font-weight: 300; color: var(--text);
  }
  .intro--left { left: 23px; }
  .intro--right { left: 261px; }
  .intro p { margin-bottom: 13px; }
  .intro b { font-weight: 400; font-size: 10px; color: var(--text-strong); }

  .services-title {
    position: absolute; left: 0; top: 354px; width: 100%;
    text-align: center; font-size: 14.5px; font-weight: 600; color: var(--accent);
  }
  .service {
    position: absolute; top: 400px; width: 150px; margin-left: -75px;
    text-align: center;
  }
  .service--plan { left: 95px; }
  .service--cost { left: 242px; }
  .service--risk { left: 387px; }
  .service h3 {
    font-size: 10.5px; font-weight: 600; color: var(--heading); margin-bottom: 8px;
  }
  .service li {
    list-style: none; font-size: 7.8px; line-height: 14.4px;
    font-weight: 300; color: var(--text); white-space: nowrap;
  }

  .tools {
    position: absolute; left: 26px; right: 24px; top: 567px;
    display: flex; justify-content: space-between; align-items: center;
  }
  .tool {
    display: flex; align-items: center; gap: 3px;
    font-size: 8.5px; font-weight: 600; color: var(--navy);
  }
  .tool__dot { width: 8px; height: 8px; background: var(--heading); }
  .tool__dot--round { border-radius: 50%; }

  .footer {
    position: absolute; left: 0; bottom: 0; width: 100%; height: 77px;
    background: var(--band);
    display: flex; align-items: flex-start; justify-content: center;
    padding-top: 22px;
    color: #fff; font-size: 14px; font-weight: 300;
  }
</style>
</head>
<body>
  <main class="flyer">
    <p class="tagline">
      Our <strong>goal</strong> is to make<br>
      <strong>successful</strong> project delivery<br>
      more <strong>achievable</strong> and <strong>repeatable</strong>.
    </p>
    <div class="band band--top"></div>

    <div class="brand">
      <div class="brand__mark"></div>
      <div class="brand__name">Corvane Project</div>
      <div class="brand__sub">SERVICES</div>
    </div>

    <div class="hero" role="img" aria-label="Photo of hands reviewing project documents with pens"></div>
    <div class="band band--mid"></div>

    <section class="intro intro--left">
      <p><b>Corvane Project Services Ltd</b> is a leading project control consultancy based in Co Cork Ireland.</p>
      <p>For over 20 years we have been <b>helping our clients</b> to deliver complex projects and programs throughout mainland Europe.</p>
    </section>
    <section class="intro intro--right">
      <p>We are <b>passionate</b> about empower organisations to achieve their objectives, <b>on time and on budget</b></p>
      <p>We are continually innovating, evolving and learning, utilize the latest industry tools and techniques to <b>deliver real value to our clients</b></p>
    </section>

    <h2 class="services-title">Corvane Project Services are happy to provide</h2>

    <section class="service service--plan">
      <h3>Planning and Scheduling</h3>
      <ul>
        <li>Tender Planning</li>
        <li>Interactive Planning / Pull Planning</li>
        <li>EPCMV Planning &amp; Scheduling</li>
        <li>Schedule Earned Value Management</li>
        <li>Independent Schedule Quality Assessment</li>
        <li>Schedule Risk Analysis (Monte Carlo)</li>
        <li>Planning &amp; Scheduling Training</li>
      </ul>
    </section>
    <section class="service service--cost">
      <h3>Cost Control</h3>
      <ul>
        <li>Estimating &amp; Forecasting</li>
        <li>Change Management</li>
        <li>Earned Value Analysis</li>
        <li>Progress Reporting</li>
        <li>Cost Risk Analysis</li>
      </ul>
    </section>
    <section class="service service--risk">
      <h3>Management of Risk (Solvaro)</h3>
      <ul>
        <li>Risk Management Policies &amp; Procedures</li>
        <li>Risk Management Strategy</li>
        <li>Risk Registers</li>
        <li>Risk Improvement Planning</li>
        <li>Risk Response and Communication</li>
        <li>Risk Management Training</li>
      </ul>
    </section>

    <div class="band band--bottom"></div>

    <div class="tools">
      <span class="tool">Tallowby</span>
      <span class="tool"><span class="tool__dot"></span>Quenfield</span>
      <span class="tool"><span class="tool__dot"></span>Brisklane</span>
      <span class="tool">Harrowmere</span>
      <span class="tool">Penwick</span>
      <span class="tool"><span class="tool__dot tool__dot--round"></span>Solvaro</span>
    </div>

    <footer class="footer">Address and contact data</footer>
  </main>
</body>
</html>
```